Product Insert / Thank You

I'm looking for a small card to be designed that will be included with our product when it ships. It will be 2 sided with 1 side being a "thank you" with our logo and the other side containing the following text:We would love to hear your feedback! For every review we receive on our products, we donate 100% of the proceeds of your order to TIDEWELL -- a non profit organization dedicated to preserving our oceans!If you are not 100% satisfied with your purchase or have any problems, we will always resolve your issue. please contact us via Brindle if you need assistance.Insert needs to be well organized and information presented in a clear and visually appealing way.
Target Market(s)
Women, aged 24-45
Colors
Designer to choose colors to be used in the design.
Look and feel

```html
<!DOCTYPE html>
<html lang="en">
<head>
<meta charset="utf-8">
<title>Thank You Insert Card</title>
<link rel="stylesheet" href="https://fonts.googleapis.com/css2?family=Montserrat:wght@800&family=Libre+Baskerville:ital,wght@0,400;0,700;1,400&display=swap">
<style>
  :root {
    --page: #f2f2f2;
    --card: #ffffff;
    --mint: #cfeee4;
    --peach: #f6cdb8;
    --olive: #d8cf5a;
    --lilac: #b58ad6;
    --lilac-soft: #cdb3e6;
    --ink: #2b2b2b;
    --white: #ffffff;
  }
  * { box-sizing: border-box; margin: 0; padding: 0; }
  html, body {
    width: 1200px;
    height: 796px;
    overflow: hidden;
    background: var(--page);
  }
  .spread {
    width: 1200px;
    height: 796px;
    display: flex;
    align-items: center;
    justify-content: center;
    gap: 90px;
  }
  .card {
    position: relative;
    width: 360px;
    height: 540px;
    background: var(--card);
    box-shadow: 0 10px 30px rgba(0,0,0,0.12);
    overflow: hidden;
  }
  .pattern-fill {
    position: absolute;
    inset: 0;
    background:
      linear-gradient(135deg, var(--mint) 0%, transparent 45%),
      linear-gradient(315deg, var(--peach) 0%, transparent 55%),
      linear-gradient(45deg, var(--olive) 0%, transparent 40%),
      var(--mint);
    opacity: 0.75;
  }
  /* back */
  .card-back .message {
    position: absolute;
    inset: 70px 36px;
    display: flex;
    flex-direction: column;
    justify-content: center;
    gap: 18px;
    text-align: center;
    font-family: "Libre Baskerville", serif;
    color: var(--ink);
    background: rgba(255,255,255,0.55);
    padding: 24px 20px;
  }
  .message .lead { font-size: 18px; font-weight: 700; line-height: 1.3; }
  .message p { font-size: 14px; line-height: 1.5; }
  .message .note { font-size: 11px; font-style: italic; }
  .message strong { font-weight: 700; }
  /* front */
  .card-front .pattern-fill { opacity: 0.7; }
  .thanks-block {
    position: absolute;
    left: 0;
    bottom: 0;
    width: 62%;
    height: 46%;
    background: var(--lilac);
    display: flex;
    align-items: center;
    padding-left: 32px;
  }
  .thanks-block h1 {
    font-family: "Montserrat", sans-serif;
    font-weight: 800;
    font-size: 44px;
    line-height: 0.95;
    color: var(--white);
    letter-spacing: 1px;
  }
  .brand {
    position: absolute;
    top: 150px;
    right: 48px;
    display: flex;
    align-items: center;
    gap: 10px;
  }
  .brand .dot {
    width: 18px;
    height: 18px;
    border-radius: 50%;
    background: var(--lilac-soft);
  }
  .brand .name {
    font-family: "Montserrat", sans-serif;
    font-weight: 800;
    font-size: 26px;
    color: var(--lilac-soft);
    letter-spacing: 3px;
  }
</style>
</head>
<body>
  <main class="spread">
    <section class="card card-back">
      <div class="pattern-fill" role="img" aria-label="Pastel geometric pattern of mint, peach and olive triangles"></div>
      <div class="message">
        <p class="lead">We would love to hear your feedback!</p>
        <p>For every review we receive on our products, we donate 100% of the proceeds of your order to <strong>TIDEWELL</strong>.</p>
        <p class="note">a non profit organization dedicated to preserving our oceans</p>
        <p>If you are not 100% satisfied with your purchase or have any problems, please contact us via Brindle.</p>
      </div>
    </section>

    <section class="card card-front">
      <div class="pattern-fill" role="img" aria-label="Pastel geometric pattern of mint, peach and olive triangles"></div>
      <div class="brand">
        <span class="dot"></span>
        <span class="name">ORIVA</span>
      </div>
      <div class="thanks-block">
        <h1>THANK<br>YOU</h1>
      </div>
    </section>
  </main>
</body>
</html>
```